Brightpath Business Cards

Two types of business cards:
square and rectangle.

Contact Information for Business Card

SQUARE
Square versions will not be specific to a person and will just have the clinic information on them. I'd like to have 4-5 options for printing on the back. I am using cardvale.example, and with that service you can upload multiple designs for the backs of the cards. So - same generic design on the front and different full color pictures with logo integration on the back. We have not selected final photos yet, but I will upload a couple to use for mock-ups.

RECTANGLE
These will be specific to providers. I would like to be able to switch out the name, title, and email address on my own (I can use photoshop or illustrator to do this) so that when we get new providers it is quick to get them cards. The rectangle cards could have multiple designs on the back as well. I am uploading examples of our OLD cards with our OLD logo.

Current logo will be uploaded as well.

I will upload high res photos to use as well as the setup template from the printer.

Font styles to use
Other font styles liked:
• Mayeka Demi Bold (logo); Questrial; open to other font choices

Colors
0455a3
9bcb3b

Requirements
Must have
• Blue - 654C
• Green - 376C
• Font on logo: Mayeka Demi Bold
• Other font I like: Questrial
• Open to other font choices as well.

```html
<!DOCTYPE html>
<html lang="en">
<head>
<meta charset="utf-8">
<title>Brightpath Business Cards</title>
<link rel="stylesheet" href="https://fonts.googleapis.com/css2?family=Questrial&family=Mulish:wght@500;700&family=Lexend:wght@400;500&display=swap">
<style>
  :root {
    --navy: #04305e;
    --green: #8abd24;
    --white: #ffffff;
    --rule: #333333;
    --card-edge: #8a8a8a;
  }
  * { box-sizing: border-box; margin: 0; padding: 0; }
  html, body { width: 1200px; height: 1200px; overflow: hidden; background: var(--white); }
  .sheet { position: relative; width: 1200px; height: 1200px; }
  .board {
    position: absolute; left: 0; top: 221px; width: 1200px; height: 757px;
    border: 1px solid var(--rule);
  }
  .board-divider { position: absolute; left: 589px; top: 0; width: 1px; height: 100%; background: var(--rule); }

  .card {
    position: absolute; width: 457px; height: 262px;
    border-radius: 15px; overflow: hidden;
    border: 1px solid var(--card-edge); background: var(--white);
  }
  .card--navy { background: var(--navy); border-color: var(--navy); }
  .col-left { left: 50px; }
  .col-right { left: 667px; }
  .row-top { top: 67px; }
  .row-bottom { top: 401px; }

  .top-notch { position: absolute; left: 207px; top: 0; width: 43px; height: 17px; }
  .url-band {
    position: absolute; left: 0; bottom: 0; width: 100%; height: 34px;
    background: var(--green);
    display: flex; align-items: center; justify-content: center;
    font-family: "Questrial", sans-serif; color: var(--white);
  }
  .url-band svg.band-notch { position: absolute; left: 206px; top: -17px; width: 45px; height: 18px; }
  .url-band .url-small { font-size: 14px; }
  .url-band .url-main { font-size: 19px; letter-spacing: 0.3px; }

  .brand { position: absolute; left: 0; width: 100%; text-align: center; }
  .brand-dot { display: block; margin: 0 auto; border-radius: 50%; background: var(--navy); }
  .card--navy .brand-dot { background: var(--white); }
  .brand-name {
    display: block; font-family: "Lexend", sans-serif; font-weight: 400;
    color: var(--navy); text-transform: uppercase;
  }
  .card--navy .brand-name { color: var(--white); }

  .brand--compact { top: 25px; }
  .brand--compact .brand-dot { width: 60px; height: 60px; }
  .brand--compact .brand-name { font-size: 23px; letter-spacing: 1.5px; margin-top: 12px; }

  .brand--large { top: 45px; }
  .brand--large .brand-dot { width: 82px; height: 82px; }
  .brand--large .brand-name { font-size: 30px; letter-spacing: 2px; margin-top: 16px; }

  .provider { position: absolute; left: 26px; top: 159px; font-family: "Mulish", sans-serif; color: var(--navy); }
  .provider-name { font-size: 13.5px; font-weight: 700; }
  .provider-title { font-size: 9.6px; font-weight: 500; margin-top: 3px; }
  .contact-divider { position: absolute; left: 228px; top: 147px; width: 1.5px; height: 58px; background: var(--navy); }
  .contact { position: absolute; left: 246px; top: 148px; list-style: none; font-family: "Mulish", sans-serif; font-size: 9.8px; font-weight: 500; color: var(--navy); }
  .contact li { display: flex; align-items: center; height: 13.5px; }
  .contact svg { width: 8px; height: 8px; margin-right: 2px; flex: none; }
  .contact .indent { padding-left: 10px; }
</style>
</head>
<body>
<div class="sheet">
  <div class="board">
    <div class="board-divider"></div>

    <!-- Provider card, option A -->
    <div class="card col-left row-top">
      <svg class="top-notch" viewBox="0 0 43 17"><polygon points="0,0 43,0 25,16 18,16" fill="var(--green)"/></svg>
      <div class="brand brand--compact"><span class="brand-dot"></span><span class="brand-name">Brightpath</span></div>
      <div class="provider"><div class="provider-name">Dr. Lena Marsh D.C.,CCSP</div><div class="provider-title">Certified Chiopratic Sports Physician</div></div>
      <div class="contact-divider"></div>
      <ul class="contact">
        <li><svg viewBox="0 0 8 8"><path d="M4 0.5a2.6 2.6 0 0 1 2.6 2.6C6.6 5 4 7.8 4 7.8S1.4 5 1.4 3.1A2.6 2.6 0 0 1 4 0.5z" fill="var(--green)"/><circle cx="4" cy="3.1" r="1" fill="var(--white)"/></svg>2210 NW Cedar Loop Ste #40</li>
        <li class="indent">Riverton, Oregon&nbsp;&nbsp;&nbsp;97000</li>
        <li><svg viewBox="0 0 8 8"><path d="M3 0.6C1.4 1.3 1 3 1 4s0.4 2.7 2 3.4L3.6 5.8 2.9 4 3.6 2.2z" fill="var(--green)"/></svg>555-014-2290</li>
        <li><svg viewBox="0 0 8 8"><rect x="0.5" y="1.5" width="7" height="5" fill="none" stroke="var(--green)" stroke-width="0.7"/><path d="M0.5 1.5 4 4.5 7.5 1.5" fill="none" stroke="var(--green)" stroke-width="0.7"/></svg>hello@brightpathsm.example</li>
      </ul>
      <div class="url-band"><svg class="band-notch" viewBox="0 0 45 18"><polygon points="0,18 17,1 28,1 45,18" fill="var(--green)"/></svg><span class="url-small">www.</span><span class="url-main">brightpathsm</span><span class="url-small">.example</span></div>
    </div>

    <!-- Provider card, option B -->
    <div class="card col-right row-top">
      <svg class="top-notch" viewBox="0 0 43 17"><polygon points="0,0 43,0 25,16 18,16" fill="var(--green)"/></svg>
      <div class="brand brand--compact"><span class="brand-dot"></span><span class="brand-name">Brightpath</span></div>
      <div class="provider"><div class="provider-name">Dr. Lena Marsh D.C.,CCSP</div><div class="provider-title">Certified Chiopratic Sports Physician</div></div>
      <div class="contact-divider"></div>
      <ul class="contact">
        <li><svg viewBox="0 0 8 8"><path d="M4 0.5a2.6 2.6 0 0 1 2.6 2.6C6.6 5 4 7.8 4 7.8S1.4 5 1.4 3.1A2.6 2.6 0 0 1 4 0.5z" fill="var(--green)"/><circle cx="4" cy="3.1" r="1" fill="var(--white)"/></svg>2210 NW Cedar Loop Ste #40</li>
        <li class="indent">Riverton, Oregon&nbsp;&nbsp;&nbsp;97000</li>
        <li><svg viewBox="0 0 8 8"><path d="M3 0.6C1.4 1.3 1 3 1 4s0.4 2.7 2 3.4L3.6 5.8 2.9 4 3.6 2.2z" fill="var(--green)"/></svg>555-014-2290</li>
        <li><svg viewBox="0 0 8 8"><rect x="0.5" y="1.5" width="7" height="5" fill="none" stroke="var(--green)" stroke-width="0.7"/><path d="M0.5 1.5 4 4.5 7.5 1.5" fill="none" stroke="var(--green)" stroke-width="0.7"/></svg>hello@brightpathsm.example</li>
      </ul>
      <div class="url-band"><svg class="band-notch" viewBox="0 0 45 18"><polygon points="0,18 17,1 28,1 45,18" fill="var(--green)"/></svg><span class="url-small">www.</span><span class="url-main">brightpathsm</span><span class="url-small">.example</span></div>
    </div>

    <!-- Back, navy -->
    <div class="card card--navy col-left row-bottom">
      <div class="brand brand--large"><span class="brand-dot"></span><span class="brand-name">Brightpath</span></div>
      <div class="url-band"><svg class="band-notch" viewBox="0 0 45 18"><polygon points="0,18 17,1 28,1 45,18" fill="var(--green)"/></svg><span class="url-small">www.</span><span class="url-main">brightpathsm</span><span class="url-small">.example</span></div>
    </div>

    <!-- Back, white -->
    <div class="card col-right row-bottom">
      <div class="brand brand--large"><span class="brand-dot"></span><span class="brand-name">Brightpath</span></div>
      <div class="url-band"><svg class="band-notch" viewBox="0 0 45 18"><polygon points="0,18 17,1 28,1 45,18" fill="var(--green)"/></svg><span class="url-small">www.</span><span class="url-main">brightpathsm</span><span class="url-small">.example</span></div>
    </div>
  </div>
</div>
</body>
</html>
```